Online medical reviews website needs banner advert!

We need banner advert templates for our website, www.traineepanel.net. These should meet the technical requirements of our partner (uploaded).

Our groundbreaking website allows doctors in training to rate and review their training.

The adverts should use the same modern design language and colour scheme as our website. They should use the text 'Help a junior doctor make a big decision - rate your training!'.

Vector assets should be supplied, allowing us to use alternative text in future.
Updates

Industry/Entity Type

Healthcare

Font styles to use
Other font styles liked:
• Karla

Colors
3277b5
0555a3
ffffff

Requirements
Must have
• Similar design to our website. Should be elegant & modern. Must allow future text to be easily inserted.
Should not have
• Unrelated design.

```html
<!DOCTYPE html>
<html lang="en">
<head>
<meta charset="utf-8">
<title>Trainee Panel – Banner Set</title>
<link href="https://fonts.googleapis.com/css2?family=Open+Sans:wght@400;600;700&display=swap" rel="stylesheet">
<style>
  :root {
    --brand-blue: #3a5fae;
    --brand-blue-deep: #2f519c;
    --navy: #0c2a86;
    --slate: #6c6f7b;
    --slate-dark: #5c5f6a;
    --grey-text: #8b8c90;
    --white: #ffffff;
    --field: #f6f8fb;
    --photo-a: #cfdcec;
    --photo-b: #eef2f7;
  }
  * { box-sizing: border-box; margin: 0; padding: 0; }
  html, body { width: 1200px; height: 980px; overflow: hidden; background: var(--white); }
  body { position: relative; font-family: "Open Sans", Arial, sans-serif; }

  .banner { position: absolute; overflow: hidden; background: linear-gradient(180deg, var(--field), var(--white)); box-shadow: 0 2px 8px rgba(0,0,0,.18); }
  .banner > * { position: absolute; }

  .brand { color: var(--white); font-weight: 400; letter-spacing: -.5px; display: flex; align-items: center; gap: 8px; white-space: nowrap; }
  .brand-dot { width: .55em; height: .55em; background: var(--white); display: inline-block; }

  .photo { background: linear-gradient(160deg, var(--photo-a), var(--photo-b)); }

  .headline { text-transform: uppercase; line-height: 1; font-weight: 600; }
  .headline .lead, .headline .tail { color: var(--grey-text); display: block; }
  .headline .key { color: var(--navy); display: block; font-weight: 700; }

  .cta { background: var(--slate); color: var(--white); border-radius: 999px; border: 2px solid var(--white);
         box-shadow: 0 1px 3px rgba(0,0,0,.35); display: flex; align-items: center; font-weight: 600;
         text-transform: uppercase; white-space: nowrap; }
  .cta svg { position: absolute; }

  .url { color: var(--white); white-space: nowrap; }

  /* Leaderboard */
  .leaderboard { left: 40px; top: 26px; width: 1128px; height: 104px; }
  .leaderboard .brand-block { left: 0; top: 0; width: 248px; height: 62px; background: var(--brand-blue); }
  .leaderboard .brand { left: 22px; top: 14px; font-size: 28px; }
  .leaderboard .url-band { left: 0; top: 62px; width: 248px; height: 42px; background: var(--slate); }
  .leaderboard .url { left: 56px; top: 71px; font-size: 17px; }
  .leaderboard .photo-left { left: 248px; top: 0; width: 138px; height: 104px; }
  .leaderboard .headline { left: 392px; top: 14px; text-align: center; width: 316px; }
  .leaderboard .lead { font-size: 18px; text-align: left; padding-left: 6px; }
  .leaderboard .key { font-size: 35px; letter-spacing: .5px; }
  .leaderboard .tail { font-size: 18px; text-align: right; padding-right: 8px; }
  .leaderboard .curve { right: 0; top: 0; width: 270px; height: 104px; }
  .leaderboard .photo-right { left: 944px; top: 0; width: 116px; height: 104px; }
  .leaderboard .cta { left: 718px; top: 36px; width: 238px; height: 42px; font-size: 16px; padding-left: 18px; }
  .leaderboard .cta svg { right: -14px; top: -4px; width: 44px; height: 40px; }

  /* Wide banner */
  .wide { left: 180px; top: 146px; width: 847px; height: 103px; }
  .wide .brand-block { left: 0; top: 0; width: 186px; height: 58px; background: var(--brand-blue); }
  .wide .brand { left: 24px; top: 18px; font-size: 21px; }
  .wide .url-band { left: 0; top: 58px; width: 186px; height: 45px; background: var(--slate); }
  .wide .url { left: 26px; top: 70px; font-size: 16px; }
  .wide .photo-left { left: 186px; top: 0; width: 120px; height: 103px; }
  .wide .headline { left: 310px; top: 14px; width: 280px; text-align: center; }
  .wide .lead { font-size: 17px; text-align: left; padding-left: 4px; }
  .wide .key { font-size: 31px; letter-spacing: .3px; }
  .wide .tail { font-size: 17px; text-align: right; padding-right: 4px; }
  .wide .curve { right: 0; top: 0; width: 200px; height: 103px; }
  .wide .photo-right { left: 756px; top: 0; width: 86px; height: 103px; }
  .wide .cta { left: 596px; top: 36px; width: 180px; height: 34px; font-size: 12px; padding-left: 14px; }
  .wide .cta svg { right: -10px; top: -4px; width: 34px; height: 32px; }

  /* Square */
  .square { left: 180px; top: 468px; width: 348px; height: 290px; }
  .square .header { left: 0; top: 0; width: 348px; height: 110px; }
  .square .brand { left: 40px; top: 14px; font-size: 28px; }
  .square .url { left: 96px; top: 52px; font-size: 15px; font-weight: 700; }
  .square .photo-left { left: 12px; top: 80px; width: 138px; height: 210px; }
  .square .headline { right: 40px; top: 112px; text-align: right; }
  .square .lead { font-size: 18px; }
  .square .key { font-size: 31px; line-height: .95; }
  .square .tail { font-size: 19px; line-height: 1.05; }
  .square .cta { left: 118px; top: 250px; width: 188px; height: 36px; font-size: 14px; padding-left: 14px; }
  .square .cta svg { right: -18px; top: -12px; width: 40px; height: 36px; }

  /* Skyscraper */
  .skyscraper { left: 553px; top: 264px; width: 348px; height: 698px; }
  .skyscraper .header { left: 0; top: 0; width: 348px; height: 112px; }
  .skyscraper .brand { left: 38px; top: 28px; font-size: 29px; }
  .skyscraper .headline { left: 0; top: 140px; width: 348px; text-align: center; }
  .skyscraper .lead { font-size: 27px; margin-bottom: 8px; }
  .skyscraper .key { font-size: 50px; line-height: .92; }
  .skyscraper .tail { font-size: 29px; margin-top: 8px; line-height: 1.05; }
  .skyscraper .photo-pair { left: 52px; top: 362px; width: 238px; height: 234px; }
  .skyscraper .footer { left: 0; top: 596px; width: 348px; height: 102px; background: var(--brand-blue); }
  .skyscraper .cta { left: 26px; top: 578px; width: 276px; height: 52px; font-size: 20px; padding-left: 20px; border-radius: 12px; }
  .skyscraper .cta svg { right: -40px; top: -16px; width: 60px; height: 56px; }
  .skyscraper .url { left: 0; width: 348px; text-align: center; top: 652px; font-size: 20px; }
</style>
</head>
<body>

  <!-- Leaderboard -->
  <section class="banner leaderboard" aria-label="Leaderboard banner">
    <div class="brand-block"></div>
    <div class="brand"><span>Trainee Panel</span><span class="brand-dot"></span></div>
    <div class="url-band"></div>
    <div class="url">traineepanel.net</div>
    <div class="photo photo-left" role="img" aria-label="Photo of a smiling male junior doctor in blue scrubs with a stethoscope"></div>
    <h2 class="headline"><span class="lead">Help a</span><span class="key">Junior Doctor</span><span class="tail">Make a big decision</span></h2>
    <svg class="curve" viewBox="0 0 270 104" preserveAspectRatio="none"><path d="M40 0 C20 30 10 70 0 104 L270 104 L270 0 Z" fill="var(--brand-blue)"/></svg>
    <div class="photo photo-right" role="img" aria-label="Photo of a smiling female doctor in a white coat holding a clipboard"></div>
    <div class="cta">Rate your training!
      <svg viewBox="0 0 44 40"><path d="M4 36 L14 10 L19 18 L36 4 L40 8 L23 22 L31 27 Z" fill="#111" stroke="#fff" stroke-width="1.5"/></svg>
    </div>
  </section>

  <!-- Wide banner -->
  <section class="banner wide" aria-label="Wide banner">
    <div class="brand-block"></div>
    <div class="brand"><span>Trainee Panel</span><span class="brand-dot"></span></div>
    <div class="url-band"></div>
    <div class="url">traineepanel.net</div>
    <div class="photo photo-left" role="img" aria-label="Photo of a smiling male junior doctor in blue scrubs with a stethoscope"></div>
    <h2 class="headline"><span class="lead">Help a</span><span class="key">Junior Doctor</span><span class="tail">Make a big decision</span></h2>
    <svg class="curve" viewBox="0 0 200 103" preserveAspectRatio="none"><path d="M34 0 C16 30 8 70 0 103 L200 103 L200 0 Z" fill="var(--brand-blue)"/></svg>
    <div class="photo photo-right" role="img" aria-label="Photo of a smiling female doctor in a white coat holding a clipboard"></div>
    <div class="cta">Rate your training!
      <svg viewBox="0 0 44 40"><path d="M4 36 L14 10 L19 18 L36 4 L40 8 L23 22 L31 27 Z" fill="#111" stroke="#fff" stroke-width="1.5"/></svg>
    </div>
  </section>

  <!-- Square -->
  <section class="banner square" aria-label="Square banner">
    <svg class="header" viewBox="0 0 348 110" preserveAspectRatio="none">
      <path d="M0 0 H348 V82 C240 84 90 92 0 110 Z" fill="var(--slate)"/>
      <path d="M0 0 H348 V74 C240 76 90 82 0 98 Z" fill="var(--brand-blue)"/>
    </svg>
    <div class="photo photo-left" role="img" aria-label="Photo of a smiling male junior doctor in blue scrubs with arms crossed"></div>
    <div class="brand"><span>Trainee Panel</span><span class="brand-dot"></span></div>
    <div class="url">www.traineepanel.net</div>
    <h2 class="headline"><span class="lead">Help a</span><span class="key">Junior<br>Doctor</span><span class="tail">Make a big<br>decision</span></h2>
    <div class="cta">Rate your training!
      <svg viewBox="0 0 44 40"><path d="M4 36 L14 10 L19 18 L36 4 L40 8 L23 22 L31 27 Z" fill="#111" stroke="#fff" stroke-width="1.5"/></svg>
    </div>
  </section>

  <!-- Skyscraper -->
  <section class="banner skyscraper" aria-label="Skyscraper banner">
    <svg class="header" viewBox="0 0 348 112" preserveAspectRatio="none">
      <path d="M0 0 H348 V96 C240 84 100 86 0 112 Z" fill="var(--slate)"/>
      <path d="M0 0 H348 V86 C240 74 100 76 0 100 Z" fill="var(--brand-blue)"/>
    </svg>
    <div class="brand"><span>Trainee Panel</span><span class="brand-dot"></span></div>
    <h2 class="headline"><span class="lead">Help a</span><span class="key">Junior<br>Doctor</span><span class="tail">Make a big<br>decision</span></h2>
    <div class="footer"></div>
    <div class="photo photo-pair" role="img" aria-label="Photo of a male junior doctor in blue scrubs and a female doctor in a white coat"></div>
    <div class="cta">Rate your training!
      <svg viewBox="0 0 44 40"><path d="M4 36 L14 10 L19 18 L36 4 L40 8 L23 22 L31 27 Z" fill="#111" stroke="#fff" stroke-width="1.5"/></svg>
    </div>
    <div class="url">www.traineepanel.net</div>
  </section>

</body>
</html>
```